The Deskwell (A new and exciting small Business support solution) Business Cards

The Deskwell Business Card Design

About us:
The Deskwell is a small business support solution, assisting businesses with any marketing, office management and human resource skills.

Objective
To be a small business lifesaver, to relieve busy professionals from mundane operations so they can focus on their businesses future through complete, reliable, efficient and effective client support. To have people say WOW what did we do before The Deskwell.

Industry/Entity Type

Small Business

Colors
0355a3
33a6d7

Requirements
Must have
• Must be similar to the look and feel of my website http://www.thedeskwell.com.au/

Must have:

Blue colour is 0094FF

The Logo

A Small Business Support Solution
- Human Resources
- Office Administration
- Marketing

Marisa Holt
0487 302 615
marisaholt@thedeskwell.com.au
www.thedeskwell.com

```html
<!DOCTYPE html>
<html lang="en">
<head>
<meta charset="utf-8">
<title>The Deskwell – Business Card</title>
<link rel="stylesheet" href="https://fonts.googleapis.com/css2?family=Open+Sans:wght@300;400;600&display=swap">
<style>
  :root {
    --backdrop: #e4e6e9;
    --card: #fbfbfb;
    --edge-blue: #0094ff;
    --band-blue: #33a6d7;
    --brand-navy: #0355a3;
    --ink: #1d2733;
    --on-band: #ffffff;
  }
  html, body {
    margin: 0;
    width: 1200px;
    height: 1000px;
    overflow: hidden;
    background: var(--backdrop);
    font-family: "Open Sans", Arial, sans-serif;
  }
  .card {
    position: absolute;
    left: 100px;
    top: 214px;
    width: 1000px;
    height: 572px;
    background: var(--card);
    border-top: 9px solid var(--edge-blue);
    border-bottom: 9px solid var(--edge-blue);
    box-sizing: border-box;
    box-shadow: 0 14px 34px rgba(0,0,0,0.18);
    overflow: hidden;
  }
  .band-contact {
    position: absolute;
    left: 560px;
    top: 182px;
    width: 440px;
    height: 146px;
    background: var(--band-blue);
  }
  .band-name {
    position: absolute;
    left: 0;
    top: 272px;
    width: 560px;
    height: 140px;
    background: var(--band-blue);
  }
  .band-divider {
    position: absolute;
    left: 560px;
    top: 182px;
    width: 1px;
    height: 146px;
    background: rgba(255,255,255,0.45);
  }
  .brand {
    position: absolute;
    left: 340px;
    top: 116px;
    margin: 0;
    font-size: 50px;
    font-weight: 600;
    letter-spacing: 0.5px;
    color: var(--brand-navy);
    line-height: 1;
  }
  .holder-name {
    position: absolute;
    left: 42px;
    top: 318px;
    margin: 0;
    padding-bottom: 8px;
    width: 470px;
    border-bottom: 1.5px solid var(--on-band);
    font-size: 46px;
    font-weight: 300;
    letter-spacing: 1px;
    text-transform: uppercase;
    color: var(--on-band);
    line-height: 1;
  }
  .contact-list {
    position: absolute;
    left: 596px;
    top: 196px;
    margin: 0;
    padding: 0;
    list-style: none;
    color: var(--on-band);
    font-size: 22px;
    font-weight: 300;
  }
  .contact-list li {
    display: flex;
    align-items: center;
    height: 42px;
  }
  .contact-list svg {
    width: 24px;
    height: 24px;
    margin-right: 16px;
    flex: none;
  }
  .services {
    position: absolute;
    left: 560px;
    top: 344px;
    color: var(--band-blue);
    font-weight: 300;
  }
  .services .tagline {
    margin: 0 0 8px 0;
    font-size: 23px;
  }
  .services ul {
    margin: 0;
    padding: 0 0 0 96px;
    list-style: none;
    font-size: 23px;
    line-height: 1.15;
  }
  .services li:last-child { padding-left: 60px; }
</style>
</head>
<body>
  <main class="card">
    <div class="band-contact"></div>
    <div class="band-name"></div>
    <div class="band-divider"></div>

    <h1 class="brand">The Deskwell.</h1>

    <h2 class="holder-name">Marisa Holt</h2>

    <ul class="contact-list">
      <li>
        <svg viewBox="0 0 24 24" aria-hidden="true"><path fill="#fff" d="M3 9c0-3 4-5 9-5s9 2 9 5v1.5h-4.5V8.5c-1.3-.6-2.8-.9-4.5-.9s-3.2.3-4.5.9v2H3z"/><path fill="#fff" d="M6 12h12l2 7H4z"/><circle cx="12" cy="15.5" r="2" fill="#33a6d7"/></svg>
        0487 302 615
      </li>
      <li>
        <svg viewBox="0 0 24 24" aria-hidden="true"><rect x="2.5" y="5.5" width="19" height="13" fill="none" stroke="#fff" stroke-width="1.5"/><path d="M2.5 5.5l9.5 7.5 9.5-7.5" fill="none" stroke="#fff" stroke-width="1.5"/></svg>
        marisaholt@thedeskwell.com.au
      </li>
      <li>
        <svg viewBox="0 0 24 24" aria-hidden="true"><g fill="none" stroke="#fff" stroke-width="1.4"><circle cx="12" cy="12" r="9.5"/><ellipse cx="12" cy="12" rx="4" ry="9.5"/><path d="M2.5 12h19M4 7h16M4 17h16"/></g></svg>
        www.thedeskwell.com
      </li>
    </ul>

    <section class="services">
      <p class="tagline">A&nbsp; Small Business Support Solution</p>
      <ul>
        <li>- Human Resources</li>
        <li>- Office Administration</li>
        <li>- Marketing</li>
      </ul>
    </section>
  </main>
</body>
</html>
```